Local Realtors helping sellers and buyers make the right decision

Looking for an Ad to place in our local paper, that is completely different from the traditional ads we see from realtors. My mother and I are a team and we would like to really stand out from the rest of the ads. Ideally, one that has humor in it would be great. Being that it's the largest investment most people make in their lives, we want to show that hiring us is going to be the best move sellers and buyers will make. With over 50 years of experience as full time realtors between us. We want buyers and sellers to know that they don't just hire their friend or the first realtor they meet. You'll be hiring two full time agents that are in the trenches everyday and know how to help them navigate the ever changing market.
I'm attaching some meme's that I've seen online to give you an idea of what we're looking for in regards to being funny, yet professional. I am also attaching two typical ads that are in this newspaper. We promoting ourselves as Agents, and not homes specifically in this ad. Our head shots will be used as well as our company logo and other contact information. The size of the ad we have reserved is ( 1/2 page vertical (4.7 x 12.25 inches) Please let me know what else I you may need to help

Gregory Halvorsk Sales Associate gregh.homes@pavrixmail.com Immediate Response # (908) 555-0147 Brookmere North Office 417 Larchmont Road (908) 555-0123 Ashcombe, NJ 07000 Marlene Halvorsk Sales Associate mkhal58@pavrixmail.com Immediate Response # (908) 555-0182 Brookmere North Office 417 Larchmont Road (908) 555-0123 Ashcombe, NJ 07000

Target Market(s)

Seller's and Buyers of residential property

Industry/Entity Type

Real Estate

Font styles to use
Serif

Colors
0555a3

Requirements
Must have
• Powerful, yet funny message to our targets
Nice to have
• We would like the ad to attract sellers and buyers
Should not have
• Should not be unprofessional. I know that's a broad description, but if you have to think about it not being professional, then it probably shouldn't be in there...

```html
<!DOCTYPE html>
<html lang="en">
<head>
<meta charset="utf-8">
<title>Let's Find Your Perfect Home – Newspaper Ad</title>
<link href="https://fonts.googleapis.com/css2?family=Tinos:wght@400;700&display=swap" rel="stylesheet">
<style>
  :root {
    --brand-blue: #0555a3;
    --frame-blue: #0a4c98;
    --accent-green: #3c9a3a;
    --ink: #1d1d1d;
    --paper: #ffffff;
    --stage: #ececec;
  }
  * { margin: 0; padding: 0; box-sizing: border-box; }
  html, body { width: 1200px; height: 1200px; overflow: hidden; background: var(--stage); }
  body { font-family: "Tinos", "Times New Roman", serif; color: var(--ink); }

  .canvas { position: relative; width: 1200px; height: 1200px; }

  .ad {
    position: absolute;
    left: 385px; top: 40px;
    width: 402px; height: 1048px;
    transform: scale(1.0687);
    transform-origin: top left;
    background: var(--paper);
    border: 10px solid var(--frame-blue);
  }
  .ad > * { position: absolute; }

  .brand { left: 0; right: 0; top: 34px; text-align: center; }
  .brand-name { font-size: 26px; font-weight: 700; color: var(--brand-blue); letter-spacing: 0.5px; }
  .brand-division { left: 0; right: 0; top: 84px; text-align: center; font-size: 12px; font-weight: 700; letter-spacing: 0.2px; }

  .services { left: 0; right: 0; top: 106px; text-align: center; font-size: 16.5px; line-height: 19px; }
  .services span::before { content: "•"; color: var(--accent-green); margin-right: 2px; }
  .services span + span { margin-left: 16px; }

  .hero-photo {
    left: 0; top: 150px; width: 382px; height: 338px;
    background: linear-gradient(160deg, #c9b98a 0%, #e8d49a 30%, #9fa39a 55%, #c7c3b8 75%, #8f8a80 100%);
  }

  .headline { left: 0; right: 0; top: 503px; text-align: center; color: var(--brand-blue); font-weight: 400; line-height: 38px; font-size: 40px; letter-spacing: -0.3px; }
  .headline .home { display: block; font-size: 62px; line-height: 62px; margin-top: 4px; }

  .heritage { left: 10px; width: 171px; top: 655px; text-align: right; color: var(--accent-green); font-variant: small-caps; font-size: 16px; line-height: 15px; }
  .mission { left: 10px; width: 171px; top: 703px; text-align: right; font-size: 12px; line-height: 12.8px; }
  .listing-photo {
    left: 191px; top: 653px; width: 158px; height: 135px;
    background: linear-gradient(180deg, #b9c6d6 0%, #c9cfd2 40%, #e6e6e2 55%, #6e8a3c 75%, #5d7a32 100%);
  }

  .agent { left: 32px; width: 320px; height: 80px; }
  .agent-gregory { top: 812px; }
  .agent-marlene { top: 915px; }
  .agent-photo { position: absolute; left: 0; top: 0; width: 70px; height: 80px; background: linear-gradient(180deg, #a7a9ad 0%, #c9b7a4 55%, #4e5866 100%); }
  .agent-marlene .agent-photo { background: linear-gradient(180deg, #9fb0c4 0%, #e0c7a8 55%, #7d8fae 100%); }
  .agent-info { position: absolute; left: 78px; top: 0; }
  .agent-name { color: var(--brand-blue); font-size: 13px; line-height: 12px; text-transform: uppercase; }
  .agent-title { color: var(--accent-green); font-size: 12px; line-height: 12px; }
  .contact { display: flex; align-items: center; gap: 4px; font-size: 9.3px; line-height: 14px; }
  .contact:first-of-type { margin-top: 2px; }
  .contact svg { width: 9px; height: 9px; flex: none; }

  .badge-housing { left: 322px; top: 922px; width: 26px; height: 26px; }
  .badge-member { left: 324px; top: 965px; width: 24px; height: 26px; background: var(--ink); }
</style>
</head>
<body>
<div class="canvas">
  <article class="ad">
    <div class="brand">
      <span class="brand-name">Hearthline Realty</span>
    </div>
    <p class="brand-division">RESIDENTIAL BROKERAGE</p>
    <p class="services"><span>FRANCHISING</span><span>GLOBAL LUXURY</span><br><span>INTERNATIONAL</span></p>

    <div class="hero-photo" role="img" aria-label="Photo of a surprised man in glasses and a striped shirt holding a small model house on a sunny city street"></div>

    <h1 class="headline">LET’S FIND<br>YOUR PERFECT<span class="home">HOME</span></h1>

    <p class="heritage">Fulfilling the<br>Dream of Home<br>Since 1906</p>
    <p class="mission">For over a century, home has been our purpose. It defines us and everyone in our network. Our mission will never waver — to deliver the treasure of home ethically and honestly.</p>
    <div class="listing-photo" role="img" aria-label="Photo of a white suburban house with a green lawn and front path"></div>

    <section class="agent agent-gregory">
      <div class="agent-photo" role="img" aria-label="Headshot of Gregory Halvorsk"></div>
      <div class="agent-info">
        <p class="agent-name">Gregory Halvorsk</p>
        <p class="agent-title">Sales Associate</p>
        <p class="contact"><svg viewBox="0 0 10 10"><rect x="0.5" y="2" width="9" height="6" fill="none" stroke="#0555a3"/><path d="M0.5 2 L5 5.5 L9.5 2" fill="none" stroke="#0555a3"/></svg>gregh.homes@pavrixmail.com</p>
        <p class="contact"><svg viewBox="0 0 10 10"><path d="M2 1 L4 1 L4.5 3 L3.3 4 Q4.5 6 6 6.7 L7 5.5 L9 6 L9 8 Q5 9 1 3 Z" fill="none" stroke="#0555a3"/></svg>Immediate Response # (908) 555-0147</p>
        <p class="contact"><svg viewBox="0 0 10 10"><path d="M5 9.5 Q1.5 5.5 1.5 3.8 A3.5 3.5 0 0 1 8.5 3.8 Q8.5 5.5 5 9.5 Z" fill="none" stroke="#0555a3"/><circle cx="5" cy="3.8" r="1.2" fill="#0555a3"/></svg>Brookmere North Office 417 Larchmont Road</p>
        <p class="contact"><svg viewBox="0 0 10 10"><path d="M2 1 L4 1 L4.5 3 L3.3 4 Q4.5 6 6 6.7 L7 5.5 L9 6 L9 8 Q5 9 1 3 Z" fill="none" stroke="#0555a3"/></svg>(908) 555-0123 Ashcombe, NJ 07000</p>
      </div>
    </section>

    <section class="agent agent-marlene">
      <div class="agent-photo" role="img" aria-label="Headshot of Marlene Halvorsk"></div>
      <div class="agent-info">
        <p class="agent-name">Marlene Halvorsk</p>
        <p class="agent-title">Sales Associate</p>
        <p class="contact"><svg viewBox="0 0 10 10"><rect x="0.5" y="2" width="9" height="6" fill="none" stroke="#0555a3"/><path d="M0.5 2 L5 5.5 L9.5 2" fill="none" stroke="#0555a3"/></svg>mkhal58@pavrixmail.com</p>
        <p class="contact"><svg viewBox="0 0 10 10"><path d="M2 1 L4 1 L4.5 3 L3.3 4 Q4.5 6 6 6.7 L7 5.5 L9 6 L9 8 Q5 9 1 3 Z" fill="none" stroke="#0555a3"/></svg>Immediate Response # (908) 555-0182</p>
        <p class="contact"><svg viewBox="0 0 10 10"><path d="M5 9.5 Q1.5 5.5 1.5 3.8 A3.5 3.5 0 0 1 8.5 3.8 Q8.5 5.5 5 9.5 Z" fill="none" stroke="#0555a3"/><circle cx="5" cy="3.8" r="1.2" fill="#0555a3"/></svg>Brookmere North Office 417 Larchmont Road</p>
        <p class="contact"><svg viewBox="0 0 10 10"><path d="M2 1 L4 1 L4.5 3 L3.3 4 Q4.5 6 6 6.7 L7 5.5 L9 6 L9 8 Q5 9 1 3 Z" fill="none" stroke="#0555a3"/></svg>(908) 555-0123 Ashcombe, NJ 07000</p>
      </div>
    </section>

    <svg class="badge-housing" viewBox="0 0 26 26" role="img" aria-label="Fair housing badge"><rect x="2" y="2" width="22" height="22" fill="none" stroke="#1d1d1d" stroke-width="2"/></svg>
    <div class="badge-member" role="img" aria-label="Membership badge"></div>
  </article>
</div>
</body>
</html>
```